Updated Business Card Design more modern and eye catching

looking for something more dynamic than the sterile card we have now. Please take a look at our web site www.brindlemarket.net to see what we do. only looking for the front side of the card for now. I've also attached a sample of a card with raised spot uv ink - it might be cool to incorporate something like that. Card should be bold yet serious. No frilly or scrolly stuff on it.
Updates
Target Market(s)
We do decor and signage for retail business and supermarkets. Our new name should reflect that we're hip but serious.
Contact Information for Business Card
standard business card size - horizontal preferred
Font styles to use
Requirements
Must have
- Current logo and colors cannot be changed.
Nice to have
- Must have information shown on existing card but open to some changes. Okay to consider spot uv.
Should not have
- Not busy with pictures in the background.

```html
<!DOCTYPE html>
<html lang="en">
<head>
<meta charset="utf-8">
<title>Brindle Market – Business Card</title>
<link href="https://fonts.googleapis.com/css2?family=Montserrat:wght@400;500&family=Open+Sans:wght@400&display=swap" rel="stylesheet">
<style>
  :root {
    --page: #e4e4e6;
    --card: #050505;
    --gold: #b9a244;
    --white: #f2f2f2;
    --rule: #4a4330;
    --emboss: #2a2a2a;
  }
  * { margin: 0; padding: 0; box-sizing: border-box; }
  html, body { width: 1200px; height: 900px; overflow: hidden; }
  body {
    background: var(--page);
    display: flex;
    align-items: center;
    justify-content: center;
    gap: 50px;
    font-family: "Open Sans", Arial, sans-serif;
  }
  .card {
    width: 525px;
    height: 300px;
    background: var(--card);
    border-radius: 24px;
    position: relative;
    color: var(--white);
    box-shadow: 0 6px 16px rgba(0,0,0,0.25);
  }
  /* back side */
  .card-back .emblem {
    position: absolute;
    left: 50%;
    top: 48px;
    transform: translateX(-50%);
  }
  .card-back .address {
    position: absolute;
    left: 0; right: 0;
    bottom: 42px;
    text-align: center;
    font-size: 14px;
    letter-spacing: 0.3px;
  }
  /* front side */
  .card-front {
    display: flex;
    flex-direction: column;
    align-items: center;
    padding-top: 44px;
  }
  .brand {
    display: flex;
    align-items: center;
    gap: 16px;
  }
  .brand-square {
    width: 44px;
    height: 44px;
    border: 3px solid var(--gold);
  }
  .brand-name {
    font-family: "Montserrat", Arial, sans-serif;
    font-weight: 400;
    font-size: 31px;
    letter-spacing: 3px;
    color: var(--white);
    line-height: 1;
  }
  .brand-rule {
    width: 300px;
    height: 2px;
    background: var(--gold);
    margin: 12px 0 0 60px;
  }
  .person-name {
    font-family: "Montserrat", Arial, sans-serif;
    font-weight: 500;
    font-size: 23px;
    letter-spacing: 3px;
    color: var(--gold);
    margin-top: 34px;
  }
  .person-title {
    font-size: 15px;
    margin-top: 2px;
  }
  .contact-rule {
    width: 400px;
    height: 1px;
    background: var(--rule);
    margin: 16px 0 12px;
  }
  .contact-line {
    font-size: 14.5px;
    line-height: 1.6;
    white-space: nowrap;
  }
  .label, .web { color: var(--gold); }
</style>
</head>
<body>
  <section class="card card-back" aria-label="Business card back">
    <svg class="emblem" width="140" height="140" viewBox="0 0 140 140" aria-hidden="true">
      <circle cx="70" cy="70" r="66" fill="none" stroke="var(--emboss)" stroke-width="3"/>
    </svg>
    <p class="address">4170 Commerce Way Fort Pierce, FL 34946</p>
  </section>

  <section class="card card-front" aria-label="Business card front">
    <div class="brand">
      <div class="brand-square"></div>
      <span class="brand-name">BRINDLE MARKET</span>
    </div>
    <div class="brand-rule"></div>
    <h1 class="person-name">MARLA KEANE</h1>
    <p class="person-title">Vice-President</p>
    <div class="contact-rule"></div>
    <p class="contact-line"><span class="label">P:</span> 555.310.2841 | <span class="label">M:</span> 555.270.4416 ext.3</p>
    <p class="contact-line"><span class="label">E:</span> Marla@BrindleMarket.net | <span class="web">www.BrindleMarket.net</span></p>
  </section>
</body>
</html>
```